Wren Vehicle Polishing (Mobile detail)

I need a business card made up. I'd like it to be different in some form, either raised, embossed, debossed, something cool that stands out. (preferably embossed text somewhere in it). I will be including the Initial png file. Let me know if you need the photoshop of adobe illustrator file to work with.

Information to be included: Text: XXX-XXX-XXXX Phone: XXX-XXX-XXXX Email: wrenpolishcrew@mailbox-demo.net Website: www.socialpage-demo.net/wrenpolishKTR Hours of operation: Mon - Fri 7:00AM to 8:00PM Sat - 10:00AM to 8:00PM

Target Market(s)

Mobile automotive detailing

Industry/Entity Type

Automotive

Contact Information for Business Card

Make it stand out with embossed lettering, I'd also like the background to be glossy black or matte, something that represents a shiny car, black preferred

Requirements
Must have
• A glossy background, or something.
• My logo, pick one of them that best fits your design.
Should not have
• White background,
• something that does not stand out.

```html
<!DOCTYPE html>
<html lang="en">
<head>
<meta charset="utf-8">
<title>Wren Vehicle Polishing – Business Card</title>
<link href="https://fonts.googleapis.com/css2?family=Arimo:wght@400;700&family=Tinos:wght@700&display=swap" rel="stylesheet">
<style>
  :root {
    --page-bg: #d9d4cc;
    --card-top: #2a2a2c;
    --card-mid: #0e0e10;
    --card-bottom: #050506;
    --ink: #ecebe8;
    --ink-soft: #cfcdc9;
    --brand-red: #d8352c;
    --band-red: #c8231d;
    --band-red-dark: #8f100c;
    --band-text: #f6dcd8;
    --divider: #8a8a8a;
    --rule: #b9b9b9;
    --accent-orange: #e0652a;
  }
  * { margin: 0; padding: 0; box-sizing: border-box; }
  html, body {
    width: 1200px; height: 970px; overflow: hidden;
    background: var(--page-bg);
  }
  .card {
    position: absolute; left: 75px; top: 172px;
    width: 1050px; height: 626px;
    background:
      linear-gradient(125deg, rgba(255,255,255,.16) 0%, rgba(255,255,255,.04) 30%, rgba(255,255,255,0) 31%),
      linear-gradient(160deg, var(--card-top) 0%, var(--card-mid) 55%, var(--card-bottom) 100%);
    box-shadow: 0 18px 40px rgba(0,0,0,.35);
    overflow: hidden;
    font-family: "Arimo", Arial, sans-serif;
    color: var(--ink);
  }
  .brand {
    position: absolute; left: 60px; top: 236px; width: 350px;
    display: flex; align-items: center; gap: 18px;
  }
  .brand-dot {
    width: 64px; height: 64px; border-radius: 50%;
    background: var(--accent-orange); flex: none;
  }
  .brand-name {
    font-weight: 700; font-size: 36px; line-height: 1.1; color: var(--ink);
  }
  .divider {
    position: absolute; left: 451px; top: 92px;
    width: 2px; height: 388px; background: var(--divider);
  }
  .person { position: absolute; left: 493px; top: 128px; }
  .person-name {
    font-family: "Tinos", "Times New Roman", serif; font-weight: 700;
    font-size: 48px; color: var(--brand-red); line-height: 1;
  }
  .person-title { font-size: 33px; margin-top: 10px; color: var(--ink); }
  .contacts {
    position: absolute; left: 493px; top: 296px;
    list-style: none; font-size: 24px; color: var(--ink-soft);
  }
  .contacts li { display: flex; align-items: center; height: 42px; white-space: nowrap; }
  .contact-icon {
    width: 24px; height: 24px; margin-right: 20px; flex: none;
    background: var(--band-red); display: flex; align-items: center; justify-content: center;
  }
  .rule-silver {
    position: absolute; left: 0; top: 540px; width: 100%; height: 10px;
    background: linear-gradient(180deg, #e2e2e2, var(--rule) 50%, #7d7d7d);
  }
  .hours-band {
    position: absolute; left: 0; top: 565px; width: 100%; height: 61px;
    background: linear-gradient(180deg, var(--band-red), var(--band-red-dark));
    display: flex; align-items: center; justify-content: flex-end;
    padding-right: 74px;
    font-size: 23px; color: var(--band-text); white-space: nowrap;
  }
</style>
</head>
<body>
  <div class="card">
    <div class="brand">
      <span class="brand-dot"></span>
      <span class="brand-name">Wren Vehicle Polishing</span>
    </div>

    <div class="divider"></div>

    <div class="person">
      <div class="person-name">Marlo Tennant</div>
      <div class="person-title">Managing Director</div>
    </div>

    <ul class="contacts">
      <li>
        <span class="contact-icon">
          <svg width="14" height="14" viewBox="0 0 14 14"><path d="M3 1l2 3-1.3 1.2c.8 1.8 2.3 3.3 4.1 4.1L9 8l3 2-1 2.5C6 12.5 1.5 8 1.5 3z" fill="#fff"/></svg>
        </span>555.018.2244
      </li>
      <li>
        <span class="contact-icon">
          <svg width="16" height="14" viewBox="0 0 16 14"><rect x="4" y="1" width="8" height="4" fill="#fff"/><rect x="1" y="5" width="14" height="5" rx="1" fill="#fff"/><rect x="4" y="9" width="8" height="4" fill="#fff" stroke="#c8231d" stroke-width="1"/></svg>
        </span>555.018.2244
      </li>
      <li>
        <span class="contact-icon">
          <svg width="16" height="12" viewBox="0 0 16 12"><rect x="1" y="1" width="14" height="10" fill="#fff"/><path d="M1 1l7 6 7-6" fill="none" stroke="#c8231d" stroke-width="1.3"/></svg>
        </span>wrenpolishcrew@mailbox-demo.net
      </li>
      <li>
        <span class="contact-icon">
          <svg width="16" height="16" viewBox="0 0 16 16"><circle cx="8" cy="8" r="6.5" fill="none" stroke="#fff" stroke-width="1.5"/><path d="M1.5 8h13M8 1.5c-3 3.5-3 9.5 0 13M8 1.5c3 3.5 3 9.5 0 13" fill="none" stroke="#fff" stroke-width="1.2"/></svg>
        </span>www.socialpage-demo.net/wrenpolishKTR
      </li>
    </ul>

    <div class="rule-silver"></div>
    <div class="hours-band">Hours of Operation:- Mon - Fri 7:00AM to 8:00PM /&nbsp; Sat - 10:00AM to 8:00PM</div>
  </div>
</body>
</html>
```